Business Card Design Project

I need a new business card design for my Remodel/Design/Build company, Northgate Home Improvement, Inc. See our website: www.northgatehomeimprovement-example.com
We are an established company with a growing reputation and growing quickly. We are know for being on the forward edge of the industry, producing a great product and our "people friendly" approach.
I am looking for something cool, transitional, maybe even retro that captures the imagination, shows our sleek creativity and streamlined approach as well as communicates stability and trustworthiness.
Updates

Stainless steel business card design would be cool.

Please have all future designs with full logo colors and shown on a stainless steel business card.  Also, logo and tag line will most likely be printed with spot uv, so layers will be necessary.  Thank you.

Target Market(s)

30-65 yrs old, homeowners, appreciate fine things, median income $150+k, net worth $1+m

Industry/Entity Type

Business

Requirements
Must have
• Company Logo
Contact information
Website URL
Nice to have
• Tagline: Building Relationships and Remodeling Homes...One Client at a Time.
Double-sided okay.
Stainless steel business card.

```html
<!DOCTYPE html>
<html lang="en">
<head>
<meta charset="utf-8">
<title>Northgate Home Improvement – Business Cards</title>
<link rel="stylesheet" href="https://fonts.googleapis.com/css2?family=Arimo:ital@1&family=Mulish:wght@500;600&display=swap">
<style>
  :root {
    --page-bg: #e6e6e6;
    --steel-light: #8a8a8a;
    --steel-mid: #777777;
    --steel-dark: #5e5e5e;
    --ink: #3a3a3a;
    --ink-soft: #333333;
  }
  * { margin: 0; padding: 0; box-sizing: border-box; }
  html, body {
    width: 1200px;
    height: 900px;
    overflow: hidden;
    background: var(--page-bg);
  }
  .canvas {
    position: relative;
    width: 1200px;
    height: 900px;
  }
  .card {
    position: absolute;
    left: 317px;
    width: 560px;
    height: 317px;
    background: linear-gradient(180deg, var(--steel-light) 0%, var(--steel-mid) 55%, var(--steel-dark) 100%);
    color: var(--ink);
  }
  .card--front { top: 101px; }
  .card--back { top: 500px; }

  .brand {
    position: absolute;
    display: flex;
    align-items: center;
    gap: 12px;
    color: var(--ink-soft);
    font-family: "Mulish", sans-serif;
    font-weight: 600;
  }
  .brand__mark {
    width: 64px;
    height: 64px;
    border-radius: 50%;
    background: var(--ink-soft);
    flex: none;
  }
  .brand__name { display: flex; flex-direction: column; line-height: 1; }
  .brand__name-main { font-size: 30px; letter-spacing: 1px; }
  .brand__name-sub { font-size: 13px; letter-spacing: 2.2px; margin-top: 4px; }

  .card--front .brand { left: 34px; top: 34px; }
  .card--back .brand { left: 138px; top: 120px; }

  .tagline {
    position: absolute;
    font-family: "Arimo", sans-serif;
    font-style: italic;
    font-size: 12px;
    line-height: 17px;
    color: var(--ink-soft);
  }
  .card--front .tagline { right: 39px; top: 130px; text-align: right; }
  .card--back .tagline { left: 0; right: 0; top: 36px; text-align: center; line-height: 23px; }

  .contact {
    position: absolute;
    right: 40px;
    top: 206px;
    text-align: right;
    font-family: "Mulish", sans-serif;
    font-style: normal;
    font-weight: 500;
    font-size: 15.5px;
    line-height: 20.5px;
    color: var(--ink);
  }
  .contact__name { font-weight: 600; }

  .web {
    position: absolute;
    left: 0;
    right: 0;
    top: 280px;
    text-align: center;
    font-family: "Mulish", sans-serif;
    font-weight: 500;
    font-size: 15.5px;
    color: var(--ink);
  }
</style>
</head>
<body>
<main class="canvas">
  <section class="card card--front" aria-label="Business card front">
    <div class="brand">
      <span class="brand__mark"></span>
      <span class="brand__name">
        <span class="brand__name-main">NORTHGATE</span>
        <span class="brand__name-sub">HOME IMPROVEMENT</span>
      </span>
    </div>
    <p class="tagline">We Plan Every Detail and Renew Your Home.<br>One Room at a Time</p>
    <address class="contact">
      <div class="contact__name">Martin Calloway</div>
      <div>Phone. 012 555 0148 Fax. 012 555 0149</div>
      <div>Email. martin@northgate-example.com</div>
      <div>www.northgatehomeimprovement-example.com</div>
    </address>
  </section>

  <section class="card card--back" aria-label="Business card back">
    <p class="tagline">We Plan Every Detail and Renew Your Home.<br>One Room at a Time</p>
    <div class="brand">
      <span class="brand__mark"></span>
      <span class="brand__name">
        <span class="brand__name-main">NORTHGATE</span>
        <span class="brand__name-sub">HOME IMPROVEMENT</span>
      </span>
    </div>
    <p class="web">www.northgatehomeimprovement-example.com</p>
  </section>
</main>
</body>
</html>
```